Hi-Tech looking WordPress design for Bright Lane Technologies

We are looking for a creative WordPress design for our client Bright Lane who is a Valtreno copier and printer managed services distributer. They also provide managed IT services.

Target Market(s)

Businesses with 10+ employees

Industry/Entity Type

Printer

Number of Pages Required

1 page

Font styles to use
Sans Serif

Requirements
Must have
• My client distributes and manages Valtreno printers and copy machines to many business industries. They also manage IT network services so their site needs to be hi-tech looking. Their corporate color is Pantone 354C and I've attached their logo.
Nice to have
• A user friendly interface with a top level menu and sliders that will market their services.
Should not have
• Do NOT display the Valtreno logo in their design.

```html
<!DOCTYPE html>
<html lang="en">
<head>
<meta charset="utf-8">
<title>Bright Lane Technologies</title>
<link rel="stylesheet" href="https://fonts.googleapis.com/css2?family=Open+Sans:ital,wght@0,400;0,600;0,700;1,400&family=Roboto+Condensed:wght@400;700&family=Oswald:wght@300&display=swap">
<style>
:root{
  --green:#1ba34b;
  --green-dark:#14873c;
  --text:#5a5a5a;
  --dark:#333;
  --grey-band:#e6e8e6;
  --card:#d9dbd9;
  --footer:#dfe5df;
  --footer-bottom:#eef1ee;
  --white:#fff;
}
*{box-sizing:border-box;margin:0;padding:0}
html,body{width:866px;height:1200px;overflow:hidden}
body{position:relative;background:var(--white);font-family:"Open Sans",Arial,sans-serif;color:var(--text);font-size:10px}
.abs{position:absolute}
.head-glow{left:0;top:66px;width:866px;height:200px;background:linear-gradient(#7fb68c,#fff)}
.logo{left:53px;top:14px;display:flex;align-items:center;gap:6px;color:var(--green);font-size:27px;font-family:"Open Sans",sans-serif}
.logo-dot{width:36px;height:36px;border-radius:50%;background:var(--green)}
.social{display:flex;gap:2px}
.social span{width:18px;height:18px;background:#2a5aa8;display:block}
.social span:nth-child(2){background:#3aa0dc}
.social span:nth-child(3){background:#1c6fb0}
.btn-consult{left:556px;top:36px;width:152px;height:24px;background:var(--green);color:#fff;font-weight:700;font-size:10px;display:flex;align-items:center;justify-content:center;border-radius:2px}
.call{left:714px;top:28px;width:94px;height:38px;border-left:1px solid #e2e2e2;border-right:1px solid #e2e2e2;padding:6px 0 0 10px;font-size:10px;color:#777;line-height:1.25}
.call b{color:#222;font-weight:700}
.nav{left:53px;top:73px;width:760px;height:32px;background:linear-gradient(#fff,#ececec);border-radius:3px;box-shadow:0 1px 2px rgba(0,0,0,.2);display:flex;align-items:center;padding-left:2px}
.nav a{font-family:"Roboto Condensed",sans-serif;font-weight:700;font-size:11px;color:#555;text-decoration:none;padding:0 14px;border-right:1px solid #d5d5d5;line-height:18px}
.nav a.current{color:var(--green);padding:0 15px}
.hero{left:53px;top:113px;width:760px;height:360px;background:radial-gradient(circle at 50% 45%,#0d4f95 0%,#2b8fd1 35%,#8fd6f2 75%,#d4f1fb 100%);border-radius:3px 3px 0 0;overflow:hidden}
.hero-band{left:436px;top:244px;width:372px;height:90px;background:rgba(20,110,80,.55)}
.hero-title{left:478px;top:252px;font-family:"Oswald",sans-serif;font-weight:300;font-size:24px;line-height:23.5px;color:#fff;letter-spacing:-.5px}
.hero-caption{left:53px;top:473px;width:760px;height:26px;background:var(--green);color:#fff;font-size:11.5px;text-align:center;line-height:26px;border-radius:0 0 3px 3px}
h2{font-family:"Roboto Condensed",sans-serif;font-weight:700;color:var(--green);font-size:12.5px}
.intro-h{left:53px;top:524px;width:325px;padding-bottom:5px;border-bottom:1px solid #ccc}
.intro-p{left:53px;top:550px;width:326px;font-size:10px;line-height:16px}
.btn{background:var(--green);color:#fff;font-size:8.5px;display:flex;align-items:center;justify-content:center;border-radius:2px}
.btn-read{left:53px;top:675px;width:64px;height:19px}
.card{top:572px;width:130px;height:120px;background:var(--card);border-radius:4px;display:flex;align-items:flex-end;justify-content:center;padding-bottom:14px;text-align:center;font-family:"Roboto Condensed",sans-serif;font-weight:700;font-size:13px;color:#555;line-height:15px}
.badge{top:525px;width:88px;height:88px;border-radius:50%;background:var(--green);border:3px solid #fff;display:flex;align-items:center;justify-content:center}
.band{left:0;top:713px;width:866px;height:181px;background:var(--grey-band)}
.testi{left:53px;top:734px;width:370px;height:140px;background:var(--green);border-radius:3px;color:#fff;padding:10px 13px}
.testi h3{font-family:"Roboto Condensed",sans-serif;font-size:12.5px;font-weight:700;margin-bottom:5px}
.testi q{display:block;width:332px;font-style:italic;font-size:11.7px;line-height:17.5px;quotes:none}
.testi .who{margin-top:8px;font-weight:700;font-size:11px}
.btn-white{left:293px;top:109px;width:63px;height:19px;background:#fff;color:var(--green);font-size:8.5px;display:flex;align-items:center;justify-content:center;border-radius:2px}
.promo{left:443px;top:734px;width:370px;height:140px;background:linear-gradient(90deg,#f3f2ef 35%,#d9cfc2 60%,#a88a72 75%,#d8d6d2 100%);border-radius:3px}
.promo-text{left:456px;top:762px;font-family:"Roboto Condensed",sans-serif;font-weight:700;color:#137a35;font-size:15px;line-height:15.5px}
.promo-text .big{font-size:18px}
.btn-contact{left:454px;top:843px;width:67px;height:19px}
.news-h{left:53px;top:927px;width:565px;padding-bottom:4px;border-bottom:1px solid #ccc}
.news{top:954px;width:180px}
.news h4{font-weight:400;font-size:10.5px;color:#333}
.news .date{font-size:8.5px;color:#999;margin:3px 0 5px}
.news p{font-size:10px;line-height:15px}
.news a{display:block;margin-top:6px;color:var(--green);text-decoration:none;font-size:10px}
.video{left:638px;top:930px;width:175px;height:132px;background:#dde0dd;padding:6px 8px}
.video h2{font-size:12.5px}
.yt{left:152px;top:6px;width:12px;height:12px;background:#d43a2c;border-radius:2px}
.video-frame{left:7px;top:27px;width:161px;height:98px;background:linear-gradient(120deg,#f1f1f1,#c9ccce 60%,#8d9296);display:flex;align-items:center;justify-content:center}
.play{width:34px;height:24px;border-radius:5px;background:var(--green);display:flex;align-items:center;justify-content:center}
.footer{left:0;top:1095px;width:866px;height:80px;background:var(--footer)}
.flinks{font-size:8.5px;line-height:12px;color:#333}
.newsletter-input{left:553px;top:1129px;width:200px;height:19px;background:#fff;border:1px solid #ddd;font-size:8.5px;padding-left:8px;line-height:17px;color:#333}
.btn-join{left:758px;top:1129px;width:54px;height:19px;font-weight:700;font-size:10px}
.bottom{left:0;top:1175px;width:866px;height:25px;background:var(--footer-bottom);font-size:8.5px;color:#555;padding:7px 0 0 51px}
</style>
</head>
<body>
<div class="abs head-glow"></div>

<div class="abs logo"><span class="logo-dot"></span><span>Bright Lane</span></div>
<div class="abs social" style="left:724px;top:5px"><span></span><span></span><span></span></div>
<div class="abs btn-consult">REQUEST A CONSULTATION</div>
<div class="abs call">Call Us<br><b>816.555.0142</b></div>

<nav class="abs nav">
  <a class="current">HOME</a><a>WHY US</a><a>PRODUCTS &amp; SERVICES</a><a>ECO</a><a>TESTIMONIALS</a><a>NEWS</a><a>HELPING HANDS</a><a>CONTACT US</a>
</nav>

<div class="abs hero" role="img" aria-label="Hand touching a glowing digital printer icon on a blue tech background"></div>
<div class="abs hero-band"></div>
<div class="abs hero-title">LOREM IPSUM DOLOR SIT<br>AMETCONSECTETUR<br>ADIPISCING ELIT</div>
<div class="abs hero-caption">Kansas City's trusted and independently owned office equipment and print partner since 2004.</div>

<h2 class="abs intro-h">POWER UP YOUR BUSINESS. THINK BRIGHT LANE.</h2>
<p class="abs intro-p">&nbsp;Bright Lane empowers Kansas City companies with copiers, multi-functional printers and digital imaging equipment. It's really that simple. We bring our expertise to your business – simplifying your business' document management systems. Find out how we can streamline your business with our complimentary Managed Print Services. Make the switch to Bright Lane and see how we can help your business thrive.</p>
<div class="abs btn btn-read">READ MORE</div>

<div class="abs card" style="left:410px">SHOW ME YOUR<br>MACHINES</div>
<div class="abs card" style="left:546px">HOW TO CHOOSE<br>A COPIER</div>
<div class="abs card" style="left:683px">FEATURES OF<br>MULTIFUNCTION<br>DEVICES</div>

<div class="abs badge" style="left:431px">
  <svg width="40" height="36" viewBox="0 0 40 36"><rect x="10" y="2" width="20" height="9" fill="#fff"/><rect x="2" y="11" width="36" height="15" rx="3" fill="#fff"/><rect x="10" y="20" width="20" height="14" fill="#fff" stroke="#1ba34b" stroke-width="2"/><line x1="14" y1="26" x2="26" y2="26" stroke="#1ba34b" stroke-width="2"/><line x1="14" y1="30" x2="26" y2="30" stroke="#1ba34b" stroke-width="2"/></svg>
</div>
<div class="abs badge" style="left:567px">
  <svg width="30" height="40" viewBox="0 0 30 40"><rect x="2" y="4" width="26" height="34" fill="none" stroke="#fff" stroke-width="2"/><rect x="9" y="1" width="12" height="6" fill="#fff"/><g stroke="#fff" stroke-width="2"><line x1="7" y1="14" x2="10" y2="14"/><line x1="13" y1="14" x2="23" y2="14"/><line x1="7" y1="20" x2="10" y2="20"/><line x1="13" y1="20" x2="23" y2="20"/><line x1="7" y1="26" x2="10" y2="26"/><line x1="13" y1="26" x2="23" y2="26"/><line x1="7" y1="32" x2="10" y2="32"/><line x1="13" y1="32" x2="23" y2="32"/></g></svg>
</div>
<div class="abs badge" style="left:704px">
  <svg width="40" height="38" viewBox="0 0 40 38"><rect x="26" y="2" width="11" height="11" fill="#fff"/><rect x="15" y="12" width="11" height="11" fill="#fff"/><rect x="3" y="25" width="11" height="11" fill="#fff"/><rect x="3" y="15" width="7" height="7" fill="#fff"/><path d="M20 12 L31 8 M14 30 L20 23 M10 18 L15 17 M26 17 L36 17" stroke="#fff" stroke-width="2" fill="none"/></svg>
</div>

<div class="abs band"></div>
<div class="abs testi">
  <h3>TESTIMONIALS</h3>
  <q>“We call our new printer "Sunny" and she has truly transformed our office! Since Sunny arrived, our team can print large format pages in full colour and the scan/fax tools have helped us go fully digital.”</q>
  <div class="who">- Dana, Marketing Agency</div>
  <div class="abs btn-white">READ MORE</div>
</div>
<div class="abs promo" role="img" aria-label="Smiling customer support agent wearing a headset"></div>
<div class="abs promo-text">MAKE THE SWITCH TO<br>BRIGHT LANE AND SEE<br><span class="big">HOW WE CAN HELP</span><br>YOUR BUSINESS THRIVE.</div>
<div class="abs btn btn-contact">CONTACT US</div>

<h2 class="abs news-h">LATEST NEWS</h2>
<div class="abs news" style="left:53px"><h4>Lorem ipsum dolor sit amet</h4><div class="date">12.06.2016</div><p>consectetur adipiscing elit, sed do eiusmod tempor incididunt ut labore et dolore magna aliqua.</p><a>Read more</a></div>
<div class="abs news" style="left:248px"><h4>Lorem ipsum dolor sit amet</h4><div class="date">12.06.2016</div><p>consectetur adipiscing elit, sed do eiusmod tempor incididunt ut labore et dolore magna aliqua.</p><a>Read more</a></div>
<div class="abs news" style="left:442px"><h4>Lorem ipsum dolor sit amet</h4><div class="date">12.06.2016</div><p>consectetur adipiscing elit, sed do eiusmod tempor incididunt ut labore et dolore magna aliqua.</p><a>Read more</a></div>

<div class="abs video">
  <h2>OUR VIDEO</h2>
  <span class="abs yt"></span>
  <div class="abs video-frame" role="img" aria-label="Video still of a woman using an office copier">
    <div class="play"><svg width="12" height="14" viewBox="0 0 12 14"><path d="M1 1 L11 7 L1 13Z" fill="#fff"/></svg></div>
  </div>
</div>

<div class="abs footer"></div>
<h2 class="abs" style="left:55px;top:1106px;font-size:10px">QUICK LINKS</h2>
<div class="abs flinks" style="left:56px;top:1127px">Home<br>Why Us<br>Products &amp; Services</div>
<div class="abs flinks" style="left:154px;top:1127px">Eco<br>Testimonials<br>News</div>
<div class="abs flinks" style="left:218px;top:1127px">Helping Hands<br>Contact Us</div>
<h2 class="abs" style="left:323px;top:1106px;font-size:10px">CORPORATE OFFICE</h2>
<div class="abs flinks" style="left:323px;top:1127px">BRIGHT LANE TECHNOLOGIES, INC.<br>1420 Meridian Ave Suite 200, Kansas City, MO 64108<br>Phone: 816.555.0142</div>
<h2 class="abs" style="left:553px;top:1106px;font-size:10px">JOIN OUR NEWSLETTER</h2>
<div class="abs newsletter-input">Enter email address</div>
<div class="abs btn btn-join">JOIN</div>

<div class="abs bottom">Copyright ©2016 Bright Lane Technologies, Inc. All Rights Reserved</div>
<div class="abs social" style="left:752px;top:1178px"><span></span><span></span><span></span></div>
</body>
</html>
```